Medicated Oil packaging design

We are looking for a new packaging design for our medicated oil, known as Calmera Balm.
- Plastic box packaging with inserts to hold the small bottle in place in the middle.
- Dimension of box is L 4cm x W 4 cm x H 8cm (Not fix, please recommend a better dimension if need be)
- The information in the word document to be displayed on 2 sides of the box.
- Selling point is the exquisite bottle, with convenient roller tip for easy application of the oil within.
-Product to target mass market, but should have a classy view/ up market outlook.
-Product to be displayed from top view and side view.
- Actual bottle is 6cm long (capped) and 1.5cm in diameter
Updates

Project Deadline Extended
Reason: Need to be overseas on a business trip, meanwhile extend the deadline since I cannot check submissions anyway.

Dear Deisgners,

Thank you for all your hard work so far. There are some wonderful designs that I would submit for voting, but a sudden new requirement came up that i need you cooperation.. I am very sorry about this. Therefore i am increasing the budget allocated for this. 

The new requirement is fairly straightforward, I have uploaded a new file called Dr photo, this person is a Chinese Physician who formulated the product. His name is Mr Lim Boon Teck. I need to include his photo on the product, as long as his face is shown will be adequate.

Meanwhile will be extending this project but a few days to cater to the new requirement. Sincere apologies and most gratitude for your hard work. Thanks a million!!

Project Deadline Extended
Reason: Added a new requirement, need to include the photo of the formulator of the product, Mr Lim Boon Teck, onto the product. See upload for the file 'Dr photo'. Also added more budget for this. Design away~ Thanks!

Target Market(s)

Mass market, to be sold at all sorts of pharmacies, convenience stores and newspaper stands.

Industry/Entity Type

Plastic

Requirements
Must have
• Must have all the wordings in the attached word document.
Make it clear that it is medicated oil, not perfume or other products.

Provide an 'insert design' for the plastic to hold the bottle in the middle of the box.
Nice to have
• Convey messages of soothing relaxation after application.
Should not have
• Nothing i can think of yet =)

```html
<!DOCTYPE html>
<html lang="en">
<head>
<meta charset="utf-8">
<title>Calmera Balm – Carton Dieline</title>
<link rel="stylesheet" href="https://fonts.googleapis.com/css2?family=Tinos:ital,wght@0,400;0,700;1,400&family=Great+Vibes&display=swap">
<style>
  :root{
    --page:#ffffff;
    --bleed:#b5df8e;
    --cut:#e3007d;
    --fold:#8a8a8a;
    --dim:#8c8c8c;
    --green-deep:#2e7a1c;
    --maroon:#6b0f12;
    --gold:#c9a033;
    --ink-dark:#1d2a12;
    --white:#ffffff;
  }
  html,body{margin:0;padding:0;width:1173px;height:1200px;overflow:hidden;background:var(--page);}
  .stage{position:relative;width:650px;height:665px;transform:scale(1.8046);transform-origin:0 0;font-family:"Tinos",serif;}
  .dieline{position:absolute;left:0;top:0;width:650px;height:665px;}
  .medicated-word{font-family:"Tinos",serif;font-weight:700;font-size:11px;letter-spacing:1.5px;fill:rgba(201,160,51,.55);}
  .brand{position:absolute;text-align:center;font-family:"Tinos",serif;font-weight:700;color:var(--green-deep);font-size:7px;letter-spacing:1.2px;}
  .brand--flip{transform:rotate(180deg);}
  .product-name{position:absolute;width:114px;text-align:center;color:var(--maroon);font-family:"Tinos",serif;font-weight:700;font-size:12.5px;line-height:1;white-space:nowrap;}
  .product-name .script{font-family:"Great Vibes",cursive;font-weight:400;color:var(--gold);font-size:14px;}
  .selling-point{position:absolute;width:76px;color:var(--white);font-family:"Tinos",serif;font-weight:700;font-size:5px;line-height:1.3;}
  .pack-size{position:absolute;color:var(--white);font-family:"Tinos",serif;font-weight:700;font-size:5px;}
  .pack-size b{font-size:8px;}
  .info{position:absolute;width:104px;color:var(--ink-dark);font-family:"Tinos",serif;font-size:4.3px;line-height:1.2;}
  .info h4{margin:3.5px 0 0;font-size:4.6px;font-weight:700;}
  .info p{margin:0;}
  .info .batch{margin-top:5px;}
  .dim-label{position:absolute;font-family:Arial,"Helvetica",sans-serif;font-size:8px;color:#555;text-align:center;}
</style>
</head>
<body>
<div class="stage">
<svg class="dieline" viewBox="0 0 650 665" xmlns="http://www.w3.org/2000/svg">
  <defs>
    <linearGradient id="bodyGreen" x1="0" y1="0" x2="0" y2="1">
      <stop offset="0" stop-color="#9fcd62"/>
      <stop offset=".35" stop-color="#6fae3a"/>
      <stop offset="1" stop-color="#2f7d1e"/>
    </linearGradient>
    <radialGradient id="glow" cx=".5" cy=".15" r=".6">
      <stop offset="0" stop-color="#f2f7c8" stop-opacity=".95"/>
      <stop offset="1" stop-color="#f2f7c8" stop-opacity="0"/>
    </radialGradient>
    <linearGradient id="maroonBand" x1="0" y1="0" x2="0" y2="1">
      <stop offset="0" stop-color="#3c0507"/>
      <stop offset="1" stop-color="#8b1a1a"/>
    </linearGradient>
    <linearGradient id="maroonBase" x1="0" y1="0" x2="1" y2="1">
      <stop offset="0" stop-color="#7a1418"/>
      <stop offset="1" stop-color="#4a0709"/>
    </linearGradient>
    <linearGradient id="bottleTone" x1="0" y1="0" x2="1" y2="0">
      <stop offset="0" stop-color="#8f9a88"/>
      <stop offset=".45" stop-color="#e4e8df"/>
      <stop offset="1" stop-color="#9aa592"/>
    </linearGradient>
    <radialGradient id="lidGlow" cx=".5" cy=".5" r=".6">
      <stop offset="0" stop-color="#ffffff"/>
      <stop offset="1" stop-color="#7fbd4b"/>
    </radialGradient>
  </defs>

  <!-- flaps: bleed fill -->
  <g class="flaps" fill="var(--bleed)" stroke="var(--bleed)" stroke-width="9" stroke-linejoin="round">
    <path d="M60 172 L62 140 Q64 118 86 118 L158 118 Q172 118 172 134 L172 172 Z"/>
    <path d="M174 172 L176 140 Q178 118 200 118 L272 118 Q286 118 286 134 L288 172 Z"/>
    <path d="M290 172 L290 62 L298 58 L298 24 Q298 12 312 12 L378 12 Q392 12 392 24 L392 58 L400 62 L400 172 Z"/>
    <path d="M404 172 L406 140 Q408 118 430 118 L500 118 Q513 118 513 134 L513 172 Z"/>
    <path d="M60 398 L62 466 Q64 488 88 488 L116 488 L146 446 L172 446 L172 398 Z"/>
    <path d="M174 398 L190 432 L228 446 L272 432 L288 398 Z"/>
    <path d="M290 398 L292 466 Q294 488 318 488 L346 488 L376 446 L400 446 L400 398 Z"/>
    <path d="M402 398 L418 432 L456 446 L500 432 L513 398 Z"/>
    <path d="M60 172 L20 180 L20 390 L60 398 Z"/>
    <rect x="60" y="172" width="455" height="226"/>
  </g>

  <!-- lid artwork -->
  <path d="M294 172 L294 66 L396 66 L396 172 Z" fill="url(#lidGlow)"/>

  <!-- glue flap -->
  <path d="M60 174 L22 181 L22 389 L60 396 Z" fill="url(#bodyGreen)"/>
  <path d="M60 174 L22 181 L22 192 L60 190 Z" fill="url(#maroonBand)"/>

  <!-- body panels -->
  <g class="panels">
    <rect x="60" y="172" width="455" height="226" fill="url(#bodyGreen)"/>
    <rect x="60" y="172" width="114" height="170" fill="url(#glow)"/>
    <rect x="174" y="172" width="114" height="170" fill="url(#glow)"/>
    <rect x="288" y="172" width="114" height="170" fill="url(#glow)"/>
    <rect x="402" y="172" width="113" height="170" fill="url(#glow)"/>
    <rect x="22" y="172" width="493" height="18" fill="url(#maroonBand)"/>
    <path d="M22 190 Q270 196 515 190" stroke="#b8323a" stroke-width=".8" fill="none"/>
  </g>

  <!-- front panel 1 -->
  <g class="front-panel">
    <text class="medicated-word" transform="translate(75 322) rotate(-90)">medicated</text>
    <rect x="94" y="226" width="50" height="110" rx="14" fill="url(#bottleTone)" role="img" aria-label="Photo of the glass roller bottle lying at an angle"/>
    <path d="M60 398 L60 346 Q118 336 174 308 L174 398 Z" fill="url(#maroonBase)"/>
    <path d="M60 342 Q118 330 174 300 L174 309 Q118 339 60 349 Z" fill="var(--white)"/>
  </g>

  <!-- front panel 3 -->
  <g class="front-panel">
    <text class="medicated-word" transform="translate(301 322) rotate(-90)">medicated</text>
    <path d="M306 334 L306 252 Q306 238 321 238 Q336 238 336 252 L336 326 Z" fill="var(--white)"/>
    <path d="M288 398 L288 346 Q346 336 402 308 L402 398 Z" fill="url(#maroonBase)"/>
    <path d="M288 342 Q346 330 402 300 L402 309 Q346 339 288 349 Z" fill="var(--white)"/>
  </g>

  <!-- cut lines -->
  <g class="cut-lines" fill="none" stroke="var(--cut)" stroke-width=".8" stroke-linejoin="round">
    <path d="M60 172 L62 140 Q64 118 86 118 L158 118 Q172 118 172 134 L172 172"/>
    <path d="M174 172 L176 140 Q178 118 200 118 L272 118 Q286 118 286 134 L288 172"/>
    <path d="M290 172 L290 62 L298 58 L298 24 Q298 12 312 12 L378 12 Q392 12 392 24 L392 58 L400 62 L400 172"/>
    <path d="M404 172 L406 140 Q408 118 430 118 L500 118 Q513 118 513 134 L513 172 L515 172 L515 398"/>
    <path d="M60 398 L62 466 Q64 488 88 488 L116 488 L146 446 L172 446 L172 398"/>
    <path d="M174 398 L190 432 L228 446 L272 432 L288 398"/>
    <path d="M290 398 L292 466 Q294 488 318 488 L346 488 L376 446 L400 446 L400 398"/>
    <path d="M402 398 L418 432 L456 446 L500 432 L513 398 L515 398"/>
    <path d="M60 172 L20 180 L20 390 L60 398"/>
  </g>

  <!-- fold lines -->
  <g class="fold-lines" stroke="var(--fold)" stroke-width=".4">
    <line x1="60" y1="172" x2="60" y2="398"/>
    <line x1="174" y1="172" x2="174" y2="398"/>
    <line x1="288" y1="172" x2="288" y2="398"/>
    <line x1="402" y1="172" x2="402" y2="398"/>
    <line x1="60" y1="172" x2="515" y2="172"/>
    <line x1="60" y1="398" x2="515" y2="398"/>
    <line x1="290" y1="62" x2="400" y2="62"/>
  </g>

  <!-- dimensions -->
  <g class="dimensions" stroke="var(--dim)" stroke-width=".5" fill="var(--dim)">
    <line x1="392" y1="12" x2="640" y2="12"/>
    <line x1="515" y1="172" x2="640" y2="172"/>
    <line x1="515" y1="398" x2="640" y2="398"/>
    <line x1="400" y1="488" x2="640" y2="488"/>
    <line x1="625" y1="12" x2="625" y2="488"/>
    <path d="M622 22 L625 12 L628 22 Z M622 478 L625 488 L628 478 Z"/>
    <line x1="578" y1="172" x2="578" y2="398"/>
    <path d="M575 182 L578 172 L581 182 Z M575 388 L578 398 L581 388 Z"/>
    <line x1="20" y1="390" x2="20" y2="630"/>
    <line x1="60" y1="398" x2="60" y2="560"/>
    <line x1="174" y1="446" x2="174" y2="560"/>
    <line x1="288" y1="398" x2="288" y2="560"/>
    <line x1="402" y1="446" x2="402" y2="560"/>
    <line x1="515" y1="398" x2="515" y2="630"/>
    <line x1="20" y1="552" x2="515" y2="552"/>
    <path d="M30 549 L20 552 L30 555 Z M50 549 L60 552 L50 555 Z M70 549 L60 552 L70 555 Z M164 549 L174 552 L164 555 Z M184 549 L174 552 L184 555 Z M278 549 L288 552 L278 555 Z M298 549 L288 552 L298 555 Z M392 549 L402 552 L392 555 Z M412 549 L402 552 L412 555 Z M505 549 L515 552 L505 555 Z"/>
    <line x1="20" y1="622" x2="515" y2="622"/>
    <path d="M30 619 L20 622 L30 625 Z M505 619 L515 622 L505 625 Z"/>
  </g>
</svg>

<!-- lid -->
<div class="brand brand--flip" style="left:300px;top:96px;width:90px;">ORVANTA</div>

<!-- front panel 1 -->
<div class="brand" style="left:60px;top:195px;width:114px;">ORVANTA</div>
<div class="product-name" style="left:60px;top:208px;">Calmera <span class="script">Balm</span></div>
<div class="selling-point" style="left:66px;top:355px;">Selling point<br>is the exquisite bottle, with convenient roller tip for easy application of the oil within</div>
<div class="pack-size" style="left:144px;top:383px;"><b>5</b> ml pack</div>

<!-- info panel 2 -->
<div class="info" style="left:180px;top:222px;">
  <h4>INDICATIONS:</h4>
  <p>Relief for headaches, giddiness, itch, runny nose and tummy aches.</p>
  <h4>DIRECTIONS:</h4>
  <p>Apply to skin, massage gently as needed. Or inhale from a tissue or tissue paper after tapping with a few drops of Soothing Fluid.</p>
  <h4>CAUTION:</h4>
  <p>For external use only. Not to be administered orally. Do not apply onto open wounds or to damaged skin. Avoid contact with eyes or on mucous membranes. Keep out of reach of children.</p>
  <h4>COMPOSITION:</h4>
  <p>Wintergreen Oil: 25%, Eucalyptus Oil:25%, Menthol:25%, White Oil:25%</p>
  <h4>Manufactured by ORVANTA PRIVATE LIMITED</h4>
  <p><b>Made in Singapore</b></p>
  <p class="batch">Mfg. Date:<br>Exp. Date:<br>Batch No.:</p>
</div>

<!-- front panel 3 -->
<div class="brand" style="left:288px;top:195px;width:114px;">ORVANTA</div>
<div class="product-name" style="left:288px;top:208px;">Calmera <span class="script">Balm</span></div>
<div class="selling-point" style="left:294px;top:355px;">Selling point<br>is the exquisite bottle, with convenient roller tip for easy application of the oil within</div>
<div class="pack-size" style="left:372px;top:383px;"><b>5</b> ml pack</div>

<!-- info panel 4 -->
<div class="brand" style="left:402px;top:195px;width:113px;">ORVANTA</div>
<div class="info" style="left:408px;top:222px;">
  <h4>INDICATIONS:</h4>
  <p>Relief for headaches, giddiness, itch, runny nose and tummy aches.</p>
  <h4>DIRECTIONS:</h4>
  <p>Apply to skin, massage gently as needed. Or inhale from a tissue or tissue paper after tapping with a few drops of Soothing Fluid.</p>
  <h4>CAUTION:</h4>
  <p>For external use only. Not to be administered orally. Do not apply onto open wounds or to damaged skin. Avoid contact with eyes or on mucous membranes. Keep out of reach of children.</p>
  <h4>COMPOSITION:</h4>
  <p>Wintergreen Oil: 25%, Eucalyptus Oil:25%, Menthol:25%, White Oil:25%</p>
  <h4>Manufactured by ORVANTA PRIVATE LIMITED</h4>
  <p><b>Made in Singapore</b></p>
  <p class="batch">Mfg. Date:<br>Exp. Date:<br>Batch No.:</p>
</div>

<!-- dimension labels -->
<div class="dim-label" style="left:560px;top:278px;width:16px;transform:rotate(-90deg);">80</div>
<div class="dim-label" style="left:20px;top:541px;width:40px;">14.3</div>
<div class="dim-label" style="left:60px;top:541px;width:114px;">40</div>
<div class="dim-label" style="left:174px;top:541px;width:114px;">40</div>
<div class="dim-label" style="left:288px;top:541px;width:114px;">40</div>
<div class="dim-label" style="left:402px;top:541px;width:113px;">39.7</div>
<div class="dim-label" style="left:20px;top:611px;width:495px;">6.85"</div>
</div>
</body>
</html>
```